Flyer für eine Imkerei
Wunderbare unkomplizierte Zusammenarbeit mit einem tollen Designer. Extrem gutes Verständnis der Grundidee, super flexibles einarbeiten eigener Verbesserungsvorschläge - einfach sehr kompetent! Danke dafür.
Zielgruppe
Ich bin Hobbyimker mit einer sehr kleinen Imkerei im Dorf. Ich biete lokalen Honig an. Der Flyer soll ein Infoflyer für Kunden und evt. Neukunden sein.
Aufgabenstellung
Bitte im Wickelfalz hochkant A4, (gefaltet also 99x210). Textbausteine sind als Datei angehängt. Bitte nur den Text nutzen, nicht Schriftgröße, Schritart etc. Ebenso ist eigenes Bildmaterial vorhanden. Ich würde mich über ein edles aber schlicht modernes Design freuen. Das Design darf gern Honigwaben (Hexagon) als Grundidee beinhalten. Bevorzugte Farbtöne sind schwarz, gold, gelb, orange (honigfarben) bis Weinrot (siehe Honigetikett auf dem Foto).

```html
<!DOCTYPE html>
<html lang="de">
<head>
<meta charset="utf-8">
<title>Feinster Honig aus dem Saaletal – Wickelfalzflyer</title>
<link rel="stylesheet" href="https://fonts.googleapis.com/css2?family=Source+Code+Pro:ital,wght@0,400;0,700;1,400;1,700&family=Open+Sans:ital,wght@0,400;0,600;1,400&display=swap">
<style>
:root{
  --bg:#d9d9db;
  --paper:#fbfbfa;
  --band:#f5d46e;
  --band-soft:#f8e3a0;
  --cream:#fcf4dc;
  --gold:#f0a81a;
  --orange:#e8900c;
  --red:#c9361f;
  --brown:#9a541a;
  --wine:#7b2218;
  --ink:#4a4038;
  --muted:#6d635a;
  --honey:#e9a82a;
  --comb:#e3a424;
  --bees:#8c5a2a;
  --leaf:#6c7a3c;
  --jar:#b5561c;
}
*{box-sizing:border-box;margin:0;padding:0}
html,body{width:1200px;height:932px;overflow:hidden;background:var(--bg)}
body{position:relative;font-family:"Open Sans",sans-serif;color:var(--ink)}
.spread{position:absolute;left:285px;width:630px;height:446px;display:flex;background:var(--paper);box-shadow:0 4px 14px rgba(0,0,0,.18)}
.spread--outside{top:13px}
.spread--inside{top:473px}
.panel{position:relative;width:210px;height:446px;overflow:hidden;background:var(--paper)}
.panel+.panel{border-left:1px solid #ece7da}
.band{position:absolute;left:0;right:0;background:linear-gradient(180deg,var(--band),var(--band-soft))}
.band--top{top:0;height:30px}
.band--bottom{bottom:0;height:34px}
.hex{position:absolute;clip-path:polygon(50% 0,100% 25%,100% 75%,50% 100%,0 75%,0 25%)}
.heading{font-family:"Source Code Pro",monospace;font-weight:700;font-style:italic;color:var(--orange);font-size:15px;line-height:1.05}
.sub{font-family:"Source Code Pro",monospace;font-weight:700;font-style:italic;color:var(--red);font-size:7.4px;line-height:1.25}
.label{font-family:"Source Code Pro",monospace;font-weight:700;font-style:italic;color:var(--red);font-size:6.6px;text-transform:uppercase;line-height:1.2;margin-top:7px}
.copy{font-size:5.3px;line-height:1.45;color:var(--muted);margin-top:2px}
.text{position:absolute;left:16px;right:16px}
.right{text-align:right}
.center{text-align:center}
/* Titelseite */
.cover{background:linear-gradient(180deg,var(--paper) 0%,var(--paper) 30%,var(--cream) 55%,var(--band-soft) 75%,var(--band) 100%)}
.cover__pre{font-family:"Source Code Pro",monospace;font-style:italic;color:var(--brown);font-size:11px;text-align:center;margin-top:40px}
.cover__title{font-family:"Source Code Pro",monospace;font-weight:700;color:var(--gold);font-size:38px;text-align:center;line-height:.95;letter-spacing:1px}
.cover__post{font-family:"Source Code Pro",monospace;font-style:italic;color:var(--brown);font-size:12px;text-align:center}
.cover__tag{margin:7px 14px 0;background:var(--brown);color:#fff3de;font-family:"Source Code Pro",monospace;font-size:7.2px;text-align:center;padding:3px 0;border-radius:2px}
.cover__foot{position:absolute;bottom:22px;left:0;right:0;text-align:center;font-family:"Source Code Pro",monospace;font-weight:700;font-style:italic;color:var(--brown);font-size:7.5px;line-height:1.3}
.fill-honey{background:radial-gradient(circle at 45% 45%,#f2c14e,var(--honey) 60%,#c9861a)}
.fill-comb{background:linear-gradient(135deg,#eeb83a,var(--comb) 60%,#c98a1b)}
.fill-bees{background:linear-gradient(135deg,#a9753a,var(--bees) 55%,#5a3a1e)}
.fill-flower{background:linear-gradient(135deg,#7b8d46,var(--leaf) 55%,#a788b6)}
.fill-jars{background:linear-gradient(135deg,#d88a2c,var(--jar) 60%,#6e2a12)}
.fill-hives{background:linear-gradient(180deg,#6fa6d8 0%,#5e8f3c 45%,#4f7a31 100%)}
.fill-yellow{background:radial-gradient(circle at 50% 50%,#f7dc2e,#e0be1a 55%,#4d6a2a)}
/* Infokasten */
.tipbox{position:absolute;left:0;right:0;top:292px;height:100px;background:var(--gold);padding:10px 14px}
.tipbox .heading{color:var(--wine);font-size:13px}
.tipbox .tip{font-family:"Source Code Pro",monospace;font-weight:700;font-style:italic;font-size:5.8px;color:#fff6e4;line-height:1.5;margin-top:5px;width:140px}
.tipbox__decor{position:absolute;right:12px;top:34px;width:38px;height:38px;background:linear-gradient(135deg,var(--wine),var(--red));border-radius:2px}
.bullet::before{content:"• ";color:var(--red)}
.contact{font-size:8px;color:var(--muted);line-height:1.3;margin-top:12px}
.phone{font-size:9px;color:var(--ink);margin-top:4px;letter-spacing:.5px}
</style>
</head>
<body>

<!-- Außenseite -->
<section class="spread spread--outside">
  <article class="panel panel--about">
    <div class="band band--top"></div>
    <div class="band band--bottom"></div>
    <div class="hex fill-flower" style="left:18px;top:8px;width:86px;height:98px" role="img" aria-label="Foto: blühende Bienenweide mit lila Blüten"></div>
    <div class="text right" style="top:118px">
      <h2 class="heading">Über uns</h2>
      <p class="sub">Herzlich Willkommen in unserer kleinen Hobbyimkerei im schönen Saaletal!</p>
      <p class="label">Bei uns erhalten Sie alles aus einer Hand.</p>
      <p class="copy">Von der sorgsamen Pflege der sensiblen Bienenvölker über die Honigernte bis hin zum fertig etikettierten Glas wird jeder Arbeitsschritt persönlich vor Ort mit größter Sorgfalt ausgeführt, um ein reines und unverfälschtes Naturprodukt zu garantieren.</p>
      <p class="label">Natürlich und schonend</p>
      <p class="copy">Wir betreiben eine sanfte und wesensgemäße Bienenhaltung. Die Bienenstöcke haben einen festen Standort auf einer sonnigen Waldlichtung. Sie werden im Saisonverlauf nicht transportiert, sondern sammeln den Nektar der Pflanzen, die hier im Saaletal ganz natürlich saisonal blühen. Das garantiert einen authentischen Honig aus unserer Heimat.</p>
    </div>
  </article>

  <article class="panel panel--contact">
    <div class="band band--top"></div>
    <div class="band band--bottom"></div>
    <div class="hex fill-jars" style="left:26px;top:8px;width:66px;height:76px" role="img" aria-label="Foto: Honiggläser im Gegenlicht"></div>
    <div class="hex fill-jars" style="left:94px;top:4px;width:82px;height:94px" role="img" aria-label="Foto: etikettierte Honiggläser"></div>
    <div class="text center" style="top:112px">
      <h2 class="heading">Probieren Sie selbst!</h2>
      <p class="copy" style="margin-top:8px;color:var(--ink)">Wurde Ihre Neugier geweckt?<br>Dann freuen wir uns, wenn Sie den reinen Geschmack unseres lokalen Produktes probieren möchten.<br>Unser Honig ist vor Ort erhältlich.</p>
      <p class="contact">Familie XYZ<br>Straße 1<br>00000 Stadt</p>
      <p class="label" style="margin-top:14px">Für Bestellungen und Abholungen erreichen Sie uns unter:</p>
      <p class="phone">0 1234 56 78 90</p>
      <p class="label" style="margin-top:16px;color:var(--orange)">Schauen Sie gern vorbei.<br>Wir freuen uns auf Sie!</p>
    </div>
  </article>

  <article class="panel cover">
    <p class="cover__pre">Feinster</p>
    <h1 class="cover__title">HONIG</h1>
    <p class="cover__post">aus dem Saaletal</p>
    <p class="cover__tag">Natürlich, Regional &amp; Direkt</p>
    <div class="hex fill-honey" style="left:56px;top:178px;width:96px;height:110px" role="img" aria-label="Foto: Honig im Glas von oben"></div>
    <div class="hex fill-comb" style="left:8px;top:264px;width:96px;height:110px" role="img" aria-label="Foto: verdeckelte Honigwabe"></div>
    <div class="hex fill-bees" style="left:106px;top:264px;width:96px;height:110px" role="img" aria-label="Foto: Bienen auf der Wabe"></div>
    <p class="cover__foot">Familie XYZ<br>Stadt XYZ</p>
  </article>
</section>

<!-- Innenseite -->
<section class="spread spread--inside">
  <article class="panel panel--honey">
    <div class="band band--top"></div>
    <div class="band band--bottom"></div>
    <div class="hex fill-hives" style="left:30px;top:4px;width:76px;height:86px" role="img" aria-label="Foto: Bienenstöcke auf einer Wiese"></div>
    <div class="hex fill-yellow" style="left:106px;top:28px;width:68px;height:78px" role="img" aria-label="Foto: Biene auf gelber Blüte"></div>
    <div class="hex fill-flower" style="left:68px;top:72px;width:68px;height:78px" role="img" aria-label="Foto: lila Blüten mit Biene"></div>
    <div class="text" style="top:158px">
      <h2 class="heading">Unser Honig</h2>
      <p class="copy" style="color:var(--ink)">Durch den festen Standort können mit zwei Honigernten im Jahr folgende Sorten angeboten werden, die den Geschmack der Saison einfangen:</p>
      <p class="label">Frühtracht – cremig:</p>
      <p class="copy">Gesammelt von den ersten Blüten des Jahres – vorwiegend Obstblüte und Raps. Für eine streichzarte Konsistenz wird dieser milde, blumige Honig vor dem Abfüllen fein-cremig gerührt.</p>
      <p class="label">Sommerblüte – flüssig &amp; cremig:</p>
      <p class="copy">Ein etwas kräftigerer und aromatischer Honig aus den Blüten des Hochsommers – vorwiegend Linde. Diesen Honig gibt es je nach Verfügbarkeit als flüssige Variante oder ebenfalls fein-cremig gerührt.</p>
    </div>
    <aside class="tipbox">
      <h3 class="heading">Gut zu Wissen:</h3>
      <p class="tip">Echter Honig kann kristallisieren. Das ist ein natürlicher Prozess und ein Zeichen für hohe Qualität. Im Wasserbad bei maximal 40°C wird er schonend wieder flüssig. Honig bitte kühl, trocken und dunkel lagern.</p>
      <div class="tipbox__decor" role="img" aria-label="Kleine Wabenverzierung in Weinrot und Honigtönen"></div>
    </aside>
  </article>

  <article class="panel panel--regional">
    <div class="band band--top"></div>
    <div class="band band--bottom"></div>
    <div class="text right" style="top:40px">
      <h2 class="heading">Warum regional?</h2>
      <p class="sub">Gutes für Sie und unsere Heimat</p>
      <p class="label">1. Für die Natur vor unserer Haustür</p>
      <p class="copy">Unsere Bienen bestäuben unzählige Pflanzen im Saaletal und sorgen so für den Erhalt der Artenvielfalt.</p>
      <p class="label">2. Absolute Transparenz</p>
      <p class="copy">Keine langen Transportwege, keine undurchsichtigen Lieferketten. Der Honig kommt direkt vom Bienenstock im Wald in Ihr Glas. Der Erlös kommt zu 100% unserer Imkerei zugute.</p>
      <p class="label">3. Der Geschmack der Heimat</p>
      <p class="copy">Jeder Löffel fängt den einzigartigen Geschmack der vielfältigen lokalen Pflanzenwelt des Saaletals ein.</p>
      <p class="label">4. Geprüfte Qualität</p>
      <p class="copy">Unser Honig wird regelmäßig in einem Fachlabor auf Qualität und Zusammensetzung untersucht. Die Analyse der Pollen bestätigt dabei die botanische und geografische Herkunft – eine Garantie für echten Honig aus der Region.</p>
    </div>
    <div class="hex fill-comb" style="left:24px;top:330px;width:100px;height:114px" role="img" aria-label="Foto: Wabenrahmen mit verdeckeltem Honig"></div>
  </article>

  <article class="panel panel--bees">
    <div class="band band--top"></div>
    <div class="band band--bottom"></div>
    <div class="hex fill-bees" style="left:26px;top:8px;width:86px;height:98px" role="img" aria-label="Foto: Bienenvolk mit Königin auf der Wabe"></div>
    <div class="text right" style="top:118px">
      <h2 class="heading">Faszinierende Bienenwelt</h2>
      <p class="sub">Wussten Sie schon?</p>
      <p class="label bullet">Bienen sind echte Vielflieger!</p>
      <p class="copy">Für Ihr 500g-Glas Honig legen sie eine Flugstrecke hin, die dreimal um die Erde reicht.</p>
      <p class="label bullet">Sie verschenken ihr Lebenswerk!</p>
      <p class="copy">Eine Biene produziert in ihrem ganzen Leben nur etwa einen halben Teelöffel Honig. Genießen Sie den Honig bewusst – es steckt viel Arbeit drin!</p>
      <p class="label bullet">Im Bienenstock regiert eine knallharte Chefin!</p>
      <p class="copy">Im Sommer legt die Königin bis zu 2.000 Eier pro Tag. Das ist mehr als ihr eigenes Körpergewicht. Ein wahrhaft produktives Management.</p>
    </div>
  </article>
</section>

</body>
</html>
```